HVL Regal Business Card Design 2020

Harbor Vale Living is looking for a business card that is clean and straight to the point but still looks high-end and attractive. We are a team comprised of management and field professionals focused on the high-end residential marketplace. We serve homeowners and trade professionals directly based out of the Metrowest/Boston area. We provide client services as well as construction/renovation services.
We are aiming for a black and white feel (white background and black text) and a matte finish with rounded edges.

We want to emphasis our vision of "Properties - Projects - Partners".
Dana Pritchell is the president of HVL

Please include the following areas we service: Boston/Cape/Newport
Please make sure to include Dana's mobile (617) 555 0143 & office number (617) 555 0187, email dana@harborvaleliving.example and website www.harborvaleliving.example

Colors

Designer to choose only greyscale colors for use in the design.

Requirements
Must have
• Include "Properties - Projects - Partners" in design

Include "After Hours Emergency Support # 1800 555 0199" with icon

```html
<!DOCTYPE html>
<html lang="en">
<head>
<meta charset="utf-8">
<title>HVL Business Card</title>
<link rel="stylesheet" href="https://fonts.googleapis.com/css2?family=Montserrat:wght@700&family=Roboto:wght@400;500&display=swap">
<style>
  :root {
    --page: #e6e6e6;
    --ink: #2a2a2a;
    --paper: #ffffff;
    --muted: #cfcfcf;
    --shadow: rgba(0,0,0,0.18);
  }
  * { margin: 0; padding: 0; box-sizing: border-box; }
  html, body { width: 1200px; height: 772px; overflow: hidden; }
  body {
    background: var(--page);
    font-family: "Roboto", Arial, sans-serif;
    position: relative;
  }
  .card {
    position: absolute;
    top: 237px;
    width: 520px;
    height: 297px;
    border-radius: 12px;
    overflow: hidden;
    box-shadow: 0 10px 28px var(--shadow);
  }
  .card--front { left: 50px; background: var(--ink); color: var(--paper); }
  .card--back { left: 630px; display: flex; }

  .brand {
    font-family: "Montserrat", Arial, sans-serif;
    font-weight: 700;
    text-align: center;
  }
  .brand__initials { display: block; font-size: 96px; line-height: 1; letter-spacing: 2px; }
  .brand__name { display: block; font-size: 15px; letter-spacing: 4px; margin-top: 8px; }

  .card--front .brand { position: absolute; left: 0; right: 0; top: 50px; }
  .service-areas {
    position: absolute;
    left: 0; right: 0; top: 194px;
    text-align: center;
    font-size: 13px;
    letter-spacing: 0.3px;
  }
  .tagline {
    position: absolute;
    left: 0; right: 0; bottom: 30px;
    text-align: center;
    font-family: "Montserrat", Arial, sans-serif;
    font-weight: 700;
    font-size: 11px;
    letter-spacing: 3px;
    color: var(--muted);
  }

  .back__logo {
    width: 44%;
    background: var(--paper);
    color: var(--ink);
    display: flex;
    align-items: center;
    justify-content: center;
  }
  .back__logo .brand__initials { font-size: 64px; }
  .back__logo .brand__name { font-size: 10px; letter-spacing: 2px; margin-top: 6px; }

  .back__contact {
    width: 56%;
    background: var(--ink);
    color: var(--paper);
    padding: 44px 0 0 30px;
    position: relative;
  }
  .contact__name {
    font-family: "Montserrat", Arial, sans-serif;
    font-weight: 700;
    font-size: 17px;
    letter-spacing: 0.3px;
  }
  .contact__title { font-size: 13px; font-weight: 500; margin: 3px 0 14px; }
  .contact__list { list-style: none; font-size: 13px; line-height: 1.55; }
  .contact__list li, .emergency { display: flex; align-items: center; gap: 8px; }
  .contact__list svg, .emergency svg { width: 12px; height: 12px; flex: none; }
  .emergency {
    position: absolute;
    left: 30px; right: 16px; bottom: 30px;
    font-size: 11px;
    line-height: 1.4;
    color: var(--muted);
    border-top: 1px solid #4a4a4a;
    padding-top: 10px;
  }
  .emergency strong { color: var(--paper); font-weight: 500; }
</style>
</head>
<body>

<section class="card card--front">
  <div class="brand">
    <span class="brand__initials">HVL</span>
    <span class="brand__name">HARBOR VALE LIVING</span>
  </div>
  <p class="service-areas">• Boston • Metrowest • South Shore • Cape • Newport</p>
  <p class="tagline">PROPERTIES - PROJECTS - PARTNERS</p>
</section>

<section class="card card--back">
  <div class="back__logo">
    <div class="brand">
      <span class="brand__initials">HVL</span>
      <span class="brand__name">HARBOR VALE LIVING</span>
    </div>
  </div>
  <div class="back__contact">
    <h1 class="contact__name">DANA PRITCHELL</h1>
    <p class="contact__title">President</p>
    <ul class="contact__list">
      <li>
        <svg viewBox="0 0 12 12" aria-hidden="true"><rect x="3" y="0.5" width="6" height="11" rx="1" fill="none" stroke="currentColor"/><line x1="5" y1="10" x2="7" y2="10" stroke="currentColor"/></svg>
        (617) 555 0143
      </li>
      <li>
        <svg viewBox="0 0 12 12" aria-hidden="true"><path d="M1 4 Q6 0 11 4 L10 5.5 L8 4.5 L8 3.5 Q6 3 4 3.5 L4 4.5 L2 5.5 Z" fill="currentColor"/><rect x="2.5" y="6" width="7" height="5" rx="1" fill="currentColor"/></svg>
        (617) 555 0187
      </li>
      <li>
        <svg viewBox="0 0 12 12" aria-hidden="true"><rect x="0.5" y="2.5" width="11" height="7" fill="none" stroke="currentColor"/><path d="M0.5 2.5 L6 7 L11.5 2.5" fill="none" stroke="currentColor"/></svg>
        dana@harborvaleliving.example
      </li>
      <li>
        <svg viewBox="0 0 12 12" aria-hidden="true"><circle cx="6" cy="6" r="5.5" fill="none" stroke="currentColor"/><ellipse cx="6" cy="6" rx="2.3" ry="5.5" fill="none" stroke="currentColor"/><line x1="0.5" y1="6" x2="11.5" y2="6" stroke="currentColor"/></svg>
        www.harborvaleliving.example
      </li>
    </ul>
    <p class="emergency">
      <svg viewBox="0 0 12 12" aria-hidden="true"><path d="M6 0.8 L11.4 10.8 L0.6 10.8 Z" fill="none" stroke="currentColor"/><line x1="6" y1="4.2" x2="6" y2="7.6" stroke="currentColor"/><circle cx="6" cy="9.2" r="0.6" fill="currentColor"/></svg>
      <span>After Hours Emergency Support # <strong>1800 555 0199</strong></span>
    </p>
  </div>
</section>

</body>
</html>
```